*YO!!! Designers Needed!!* Front Page Cover Needed for a $$Billion Dollar$$ Company

We are a manufacturer of aluminum electrolytic capacitors. We are looking to create a front page cover that will be used on our annual report. We are a publicly listed company and work with many Pinnacle 300 companies, so your work will be viewed by the BIG GUNS and EXECUTIVES around the WORLD! If selected, you may be selected for additional work.

The front page cover should be unique. If elegance, modern, bling, and creativity somehow got together and had a child, that's what the cover page would look like!

Inspired Examples attached. Check them out!

www.velmoro.com

Font styles to use
Sans Serif

Requirements
Must have
• 1. Must include the attached logo. Logo size, color, and placement are at your discretion.

2. Should include the text, '2020 Annual Report'

3. The design should incorporate the use of foil and/or be embossed. The foil can be part of the design or can be the full page. See various examples attached for reference.

4. Shall be in A4 size and vertical orientation.
Nice to have
• Feel free to add any icons or stock photos (for example capacitors or circuit boards) if needed.

Be creative here and don't be afraid to be bold! The end product will be printed and budget is not a limiting factor, so feel free to make it extravagant if needed.

Our slogan is "Think Ahead". This slogan can or cannot be part of the theme.

```html
<!DOCTYPE html>
<html lang="en">
<head>
<meta charset="UTF-8">
<title>Velmoro 2020 Annual Report Cover</title>
<link rel="stylesheet" href="https://fonts.googleapis.com/css2?family=Anton&family=Montserrat:wght@600&display=swap">
<style>
  :root {
    --backdrop: #c8c8c8;
    --paper: #f1f1f1;
    --ink: #0d0d0d;
    --white: #ffffff;
  }
  html, body {
    margin: 0;
    padding: 0;
    width: 757px;
    height: 1200px;
    overflow: hidden;
    background: var(--backdrop);
  }
  .cover {
    position: absolute;
    left: 8.5px;
    top: 121px;
    width: 740px;
    height: 957px;
    background: var(--paper);
    box-shadow: 0 4px 14px rgba(0,0,0,0.35);
    overflow: hidden;
  }
  .cover__dark-panel {
    position: absolute;
    left: 358px;
    top: 0;
    width: 382px;
    height: 957px;
    background: var(--ink);
  }
  .cover__frame {
    position: absolute;
    left: 17px;
    top: 20px;
    width: 341px;
    height: 836px;
    border: 3px solid var(--ink);
    border-right: none;
    box-sizing: border-box;
  }
  .brand {
    position: absolute;
    right: 63px;
    top: 46px;
    color: var(--white);
    font-family: "Montserrat", sans-serif;
    font-weight: 600;
    font-size: 27px;
    line-height: 1;
    letter-spacing: 1px;
  }
  .title {
    position: absolute;
    left: 0;
    top: 0;
    width: 740px;
    height: 957px;
  }
  .title text {
    font-family: "Anton", sans-serif;
  }
</style>
</head>
<body>
  <main class="cover">
    <div class="cover__dark-panel"></div>
    <div class="cover__frame"></div>

    <div class="brand">VELMORO</div>

    <svg class="title" viewBox="0 0 740 957" aria-label="2020 Annual Report">
      <defs>
        <clipPath id="light-side"><rect x="0" y="0" width="358" height="957"/></clipPath>
        <clipPath id="dark-side"><rect x="358" y="0" width="382" height="957"/></clipPath>
        <g id="title-words">
          <text x="142" y="564" font-size="288" textLength="432" lengthAdjust="spacingAndGlyphs">2020</text>
          <text x="233" y="693" font-size="97" textLength="341" lengthAdjust="spacingAndGlyphs">ANNUAL</text>
          <text x="148" y="827" font-size="129" textLength="424" lengthAdjust="spacingAndGlyphs">REPORT</text>
        </g>
      </defs>
      <use href="#title-words" fill="#0d0d0d" clip-path="url(#light-side)"/>
      <use href="#title-words" fill="#ffffff" clip-path="url(#dark-side)"/>
    </svg>
  </main>
</body>
</html>
```